Professional Sales Business looking for inspirational poster

I need an inspirational poster design for sales professionals, targeted around the phrase "Win Fast, Lose Fast". The style of the poster will be primarily minimalistic and flat with the main focus being on the phrase, however, any graphics or creative font and background styles are encouraged. Color choice is up to you.

Design Specs:
Vector files are best. If creating a vector file isn't possible, 150dpi raster images (at actual size or bigger) are good too. The poster must be in a portrait layout and scalable to the sizes of 18" X 24" and 24" X 36". Please convert all text to outlines.

Please msg me if you have any additional questions.

```html
<!DOCTYPE html>
<html lang="en">
<head>
<meta charset="utf-8">
<title>Win Fast Lose Fast – Poster Artboards</title>
<link rel="stylesheet" href="https://fonts.googleapis.com/css2?family=IM+Fell+English+SC&family=Jost:ital,wght@1,700&display=swap">
<style>
  :root {
    --workspace: #5d5d5d;
    --ink: #ffffff;
    --forest-dark: #0c3328;
    --forest: #1d4d3a;
    --road-teal: #3f8a82;
    --road-grey: #4f8f8a;
    --line-yellow: #8cc447;
    --asphalt: #2f6d6b;
  }
  * { margin: 0; padding: 0; box-sizing: border-box; }
  html, body {
    width: 1200px;
    height: 990px;
    overflow: hidden;
    background: var(--workspace);
  }
  .workspace {
    position: relative;
    width: 1200px;
    height: 990px;
  }
  .poster {
    position: absolute;
    overflow: hidden;
    outline: 1px solid #333;
  }
  .poster--tall { left: 9px; top: 5px; width: 656px; height: 985px; }
  .poster--short { left: 697px; top: 14px; width: 490px; height: 658px; }

  .poster__backdrop {
    position: absolute;
    inset: 0;
    background:
      radial-gradient(ellipse 45% 30% at 15% 42%, rgba(90,150,140,0.55), transparent 70%),
      linear-gradient(180deg,
        var(--forest-dark) 0%,
        var(--forest) 38%,
        var(--road-teal) 56%,
        var(--road-grey) 66%,
        var(--line-yellow) 72%,
        var(--asphalt) 78%,
        var(--line-yellow) 84%,
        var(--road-teal) 100%);
  }
  .poster--short .poster__backdrop {
    background:
      radial-gradient(ellipse 40% 30% at 12% 40%, rgba(90,150,140,0.55), transparent 70%),
      linear-gradient(180deg,
        var(--forest-dark) 0%,
        var(--forest) 40%,
        var(--road-teal) 62%,
        var(--road-grey) 70%,
        var(--line-yellow) 76%,
        var(--asphalt) 82%,
        var(--line-yellow) 88%,
        var(--road-teal) 100%);
  }

  .slogan { position: absolute; inset: 0; color: var(--ink); }
  .slogan__word {
    position: absolute;
    left: 0;
    right: 0;
    text-align: center;
    line-height: 1;
    white-space: nowrap;
  }
  .slogan__word--rough {
    font-family: "IM Fell English SC", Georgia, serif;
    font-weight: 400;
  }
  .slogan__word--bold {
    font-family: "Jost", "Futura", sans-serif;
    font-weight: 700;
    font-style: italic;
    letter-spacing: -0.01em;
  }

  .poster--tall .slogan__win   { top: 170px; font-size: 146px; }
  .poster--tall .slogan__fast1 { top: 300px; font-size: 143px; }
  .poster--tall .slogan__lose  { top: 411px; font-size: 162px; }
  .poster--tall .slogan__fast2 { top: 551px; font-size: 143px; }

  .poster--short .slogan__win   { top: 120px; font-size: 103px; }
  .poster--short .slogan__fast1 { top: 205px; font-size: 103px; }
  .poster--short .slogan__lose  { top: 289px; font-size: 112px; }
  .poster--short .slogan__fast2 { top: 382px; font-size: 103px; }
</style>
</head>
<body>
<main class="workspace">
  <section class="poster poster--tall">
    <div class="poster__backdrop" role="img" aria-label="Blurred photo of a winding country road through green forest, with double yellow centre lines in the foreground"></div>
    <h1 class="slogan">
      <span class="slogan__word slogan__word--rough slogan__win">WIN</span>
      <span class="slogan__word slogan__word--bold slogan__fast1">FAST</span>
      <span class="slogan__word slogan__word--rough slogan__lose">LOSE</span>
      <span class="slogan__word slogan__word--bold slogan__fast2">FAST</span>
    </h1>
  </section>

  <section class="poster poster--short">
    <div class="poster__backdrop" role="img" aria-label="Blurred photo of a winding country road through green forest, with double yellow centre lines in the foreground"></div>
    <h2 class="slogan">
      <span class="slogan__word slogan__word--rough slogan__win">WIN</span>
      <span class="slogan__word slogan__word--bold slogan__fast1">FAST</span>
      <span class="slogan__word slogan__word--rough slogan__lose">LOSE</span>
      <span class="slogan__word slogan__word--bold slogan__fast2">FAST</span>
    </h2>
  </section>
</main>
</body>
</html>
```